Clean and modern business cards

Looking for an updated business card design for my dental office “corvanta dental” . Looking for a modern clean / sleek design . I’m thinking black background but open to seeing other options . One side needs to have an appointment card . Card needs to have logo, dentist name , phone, email , address . I’ve attached couple of cards I thought were cool as well as my logo
Target Market(s)
Dental patients
Industry/Entity Type
Dentistry
Contact Information for Business Card
Phone email address

```html
<!DOCTYPE html>
<html lang="en">
<head>
<meta charset="utf-8">
<title>Corvanta Dental – Business Cards</title>
<link href="https://fonts.googleapis.com/css2?family=Inter:wght@400;500;700;800&display=swap" rel="stylesheet">
<style>
  :root{
    --stage:#e4e4e4;
    --card-white:#ffffff;
    --card-black:#141414;
    --ink:#111111;
    --rule:#7a7a7a;
    --light:#f2f2f2;
    --muted:#cfcfcf;
  }
  *{box-sizing:border-box;margin:0;padding:0}
  html,body{width:1200px;height:800px;overflow:hidden}
  body{
    background:var(--stage);
    font-family:"Inter",Arial,sans-serif;
    display:flex;align-items:center;justify-content:center;gap:48px;
  }
  .card{
    width:540px;height:309px;position:relative;overflow:hidden;
    box-shadow:0 10px 30px rgba(0,0,0,.18);
  }

  /* Appointment side */
  .appointment{background:var(--card-white);color:var(--ink)}
  .appointment__brand{
    position:absolute;top:34px;right:34px;display:flex;align-items:center;gap:10px;
  }
  .brand-dot{width:22px;height:22px;border-radius:50%;background:var(--ink)}
  .brand-name{font-weight:700;font-size:15px;letter-spacing:2px;text-transform:uppercase}
  .appointment__title{position:absolute;left:34px;top:104px;font-weight:700;font-size:19px}
  .appointment__field{
    position:absolute;left:34px;display:flex;align-items:flex-end;gap:12px;font-size:16px;
  }
  .appointment__field .line{border-bottom:1.3px solid var(--ink);height:1px;margin-bottom:4px}
  .field-date{top:148px}
  .field-date .line{width:236px}
  .field-time{top:186px}
  .field-time .line{width:236px}
  .appointment__note{
    position:absolute;left:34px;right:34px;top:224px;font-size:9.5px;
  }
  .appointment__band{
    position:absolute;left:0;right:0;bottom:0;height:62px;background:var(--card-black);
    color:var(--light);font-size:11.5px;line-height:1.45;
    display:flex;flex-direction:column;align-items:center;justify-content:center;text-align:center;
  }

  /* Contact side */
  .contact{background:var(--card-black);color:var(--light)}
  .contact__brand{
    position:absolute;top:48px;left:0;right:0;display:flex;align-items:center;justify-content:center;gap:14px;
  }
  .contact__brand .brand-dot{width:46px;height:46px;background:var(--light)}
  .contact__brand .brand-name{font-size:26px;font-weight:800;letter-spacing:3px;color:var(--light)}
  .contact__name{
    position:absolute;top:128px;left:0;right:0;text-align:center;
    font-weight:700;font-size:26px;letter-spacing:1.5px;
  }
  .contact__rule{position:absolute;left:34px;right:34px;height:1px;background:var(--rule)}
  .rule-top{top:184px}
  .rule-bottom{top:230px}
  .contact__row{
    position:absolute;left:34px;right:34px;display:flex;align-items:center;
    font-size:11px;color:var(--muted);
  }
  .row-main{top:196px;justify-content:space-between}
  .row-address{top:246px;justify-content:center}
  .contact__item{display:flex;align-items:center;gap:7px}
  .icon{width:15px;height:15px;flex:none}
</style>
</head>
<body>

  <section class="card appointment" aria-label="Appointment card">
    <div class="appointment__brand">
      <span class="brand-dot"></span>
      <span class="brand-name">Corvanta Dental</span>
    </div>
    <h2 class="appointment__title">Your next appointment is:</h2>
    <div class="appointment__field field-date"><span>Date:</span><span class="line"></span></div>
    <div class="appointment__field field-time"><span>Time:</span><span class="line"></span></div>
    <p class="appointment__note">To cancel or reschedule please notify us at least 48 hours prior to your scheduled appointment</p>
    <div class="appointment__band">
      <span>2140 Alder Ridge Rd, Winnipeg, MB | 204-555-0182</span>
      <span>www.corvantadental.ca | hello@corvantadental.ca</span>
    </div>
  </section>

  <section class="card contact" aria-label="Contact card">
    <div class="contact__brand">
      <span class="brand-dot"></span>
      <span class="brand-name">Corvanta Dental</span>
    </div>
    <h1 class="contact__name">MARISA</h1>
    <div class="contact__rule rule-top"></div>
    <div class="contact__row row-main">
      <span class="contact__item">
        <svg class="icon" viewBox="0 0 16 16"><circle cx="8" cy="8" r="8" fill="#f2f2f2"/><path d="M5.3 4.2l1.4 1.6-.7 1c.5 1.1 1.3 1.9 2.4 2.4l1-.7 1.6 1.4-.8 1.3c-2.9-.3-5.2-2.6-5.5-5.5z" fill="#141414"/></svg>
        204-555-0182
      </span>
      <span class="contact__item">
        <svg class="icon" viewBox="0 0 16 16"><circle cx="8" cy="8" r="8" fill="#f2f2f2"/><rect x="4" y="5.2" width="8" height="5.6" fill="#141414"/><path d="M4 5.4l4 3 4-3" stroke="#f2f2f2" stroke-width=".9" fill="none"/></svg>
        marisa@corvantadental.ca
      </span>
      <span class="contact__item">
        <svg class="icon" viewBox="0 0 16 16"><circle cx="8" cy="8" r="8" fill="#f2f2f2"/><circle cx="8" cy="8" r="4" fill="none" stroke="#141414" stroke-width="1"/><ellipse cx="8" cy="8" rx="1.7" ry="4" fill="none" stroke="#141414" stroke-width="1"/><path d="M4 8h8" stroke="#141414" stroke-width="1"/></svg>
        www.corvantadental.ca
      </span>
    </div>
    <div class="contact__rule rule-bottom"></div>
    <div class="contact__row row-address">
      <span class="contact__item">
        <svg class="icon" viewBox="0 0 16 16"><circle cx="8" cy="8" r="8" fill="#f2f2f2"/><path d="M8 12.5s-3-3.2-3-5.4a3 3 0 016 0c0 2.2-3 5.4-3 5.4z" fill="#141414"/><circle cx="8" cy="7" r="1.1" fill="#f2f2f2"/></svg>
        104 – 2140 Alder Ridge Rd, Winnipeg, MB R3T 0B2
      </span>
    </div>
  </section>

</body>
</html>
```